Hybrid Seed corn and Soybean Sales business needs a website.

We here at "QT Grain" feel that we need a website to show a very professional side to our customer base. Although no actual ordering will take place on this website, we would like to put Plot and field trail data on the website. Along with a brief page for each of our hybrids and a place for customers to sign up for a newsletter. The company we sell hybrids for is MarlowGrain.com... Im not sure how this process works as far as myself updating the information or having the data actually put on the website, but feel free to contact me if you need the information. I will attach the logo for the company, (QT Grain).

Target Market(s)

Farmers, "Producers", Corn and soybean production

Industry/Entity Type

Business

Coding

Coded - Design and coding required

Number of Pages Required

5+ page

Colors
f78f20
ffffff

Requirements
Nice to have
• Similar layout to http://www.marlowgrain.example/
• And it would be nice to incorporate our story into the website
• http://www.marlowgrain.example/our-story/marlow-today/

```html
<!DOCTYPE html>
<html lang="en">
<head>
<meta charset="utf-8">
<title>QT Grain — Hybrid Seeds of Corn &amp; Soybean</title>
<link href="https://fonts.googleapis.com/css2?family=Arimo:wght@400;700&display=swap" rel="stylesheet">
<style>
:root{
  --orange:#f78f20;
  --green:#6aab1c;
  --text:#333333;
  --body:#444444;
  --rule:#e6e6e6;
  --nav-top:#5c5c5c;
  --nav-bottom:#3d3d3d;
  --footer:#1b1a1a;
  --white:#ffffff;
}
*{margin:0;padding:0;box-sizing:border-box}
html,body{width:806px;height:1200px;overflow:hidden;background:var(--white)}
body{position:relative;font-family:"Arimo",Arial,sans-serif;color:var(--text)}
.abs{position:absolute}

.brand{left:0;width:806px;top:22px;text-align:center;font-weight:700;font-size:22px;letter-spacing:2px;color:var(--orange)}
.brand .dot{display:inline-block;width:12px;height:12px;border-radius:50%;background:var(--green);margin-right:8px;vertical-align:2px}

.main-nav{left:50px;top:84px;width:706px;height:42px;background:linear-gradient(var(--nav-top),var(--nav-bottom))}
.main-nav a{position:absolute;top:12px;font-size:10px;color:var(--white);text-decoration:none;transform:translateX(-50%);white-space:nowrap;line-height:22px;top:12px}
.main-nav a.active{background:var(--green);width:50px;text-align:center}

.hero{left:0;top:126px;width:806px;height:376px;background:linear-gradient(180deg,#8fa7bd 0%,#b9c6cf 30%,#7c9a52 55%,#3f6a1c 80%,#2f5212 100%)}
.hero-title{right:50px;top:356px;text-align:right;font-size:22px;line-height:30px;color:var(--white);text-transform:uppercase}
.hero-arrow{top:424px;width:26px;height:26px}

.section-title{left:0;width:806px;text-align:center;font-size:19px;text-transform:uppercase;color:var(--text)}
.section-title span{color:var(--orange)}
.about-text{left:59px;width:686px;top:572px;text-align:center;font-size:9px;line-height:17px;color:var(--body)}
.btn{left:362px;top:633px;width:81px;height:21px;background:var(--green);color:var(--white);font-size:8.5px;text-align:center;line-height:21px}
.rule{height:1px;background:var(--rule)}

.video-main{left:86px;top:744px;width:344px;height:194px;background:radial-gradient(ellipse at 25% 85%,#f6b94a 0%,#c65a16 25%,#5a2a14 60%,#2c1a12 100%)}
.video-bar{left:86px;top:918px;width:344px;height:20px;background:linear-gradient(#d8d8d8,#a9a9a9)}
.thumb{width:131px;height:91px}
.play{position:absolute;left:50%;top:50%;transform:translate(-50%,-50%)}

.partners-title{left:50px;top:1006px;font-size:12px;text-transform:uppercase}
.partners-title span{color:var(--orange)}
.partners-text{left:50px;top:1030px;width:300px;font-size:8px;line-height:15px;color:var(--body)}
.partner{top:1004px;width:121px;height:58px;border:1px solid #dddddd;text-align:center;line-height:56px;font-size:14px;font-weight:700;color:var(--text)}
.partner .dot{display:inline-block;width:10px;height:10px;margin-right:6px;vertical-align:0}

.site-footer{left:0;top:1099px;width:806px;height:101px;background:var(--footer)}
.social{top:1122px;width:24px;height:24px;border-radius:50%}
.copyright{left:51px;top:1164px;font-size:8px;color:#bbbbbb}
.newsletter-title{left:584px;top:1127px;font-size:10px;color:var(--white);text-transform:uppercase}
.newsletter-input{left:584px;top:1152px;width:149px;height:21px;border:1px solid #555;background:#161616;color:#888;font-size:7.5px;line-height:19px;padding-left:9px}
.newsletter-btn{left:733px;top:1152px;width:22px;height:21px;background:#5a5a5a}
</style>
</head>
<body>

<header>
  <div class="abs brand"><span class="dot"></span>QT GRAIN</div>
  <nav class="abs main-nav">
    <a class="active" href="#" style="left:90px">Home</a>
    <a href="#" style="left:156px">Our Story</a>
    <a href="#" style="left:228px">Friends</a>
    <a href="#" style="left:308px">Products</a>
    <a href="#" style="left:418px">Events &amp; Getaways</a>
    <a href="#" style="left:525px">Testimonials</a>
    <a href="#" style="left:611px">Contact</a>
  </nav>
</header>

<section>
  <div class="abs hero" role="img" aria-label="Young corn plant in a green field under a cloudy sky"></div>
  <h1 class="abs hero-title" style="font-weight:400">We sell hybrid seeds of<br>corn &amp; soybean</h1>
  <svg class="abs hero-arrow" style="left:699px" viewBox="0 0 26 26"><circle cx="13" cy="13" r="13" fill="#fff" opacity=".9"/><path d="M15 7l-6 6 6 6" fill="none" stroke="#666" stroke-width="1.2"/></svg>
  <svg class="abs hero-arrow" style="left:729px" viewBox="0 0 26 26"><circle cx="13" cy="13" r="13" fill="#fff" opacity=".9"/><path d="M11 7l6 6-6 6" fill="none" stroke="#666" stroke-width="1.2"/></svg>
</section>

<section>
  <h2 class="abs section-title" style="top:541px;font-weight:400">About <span>QT Grain</span></h2>
  <p class="abs about-text">Sed ut perspiciatis unde omnis iste natus error sit voluptatem accusantium doloremque laudantium, totam rem aperiam, eaque ipsa quae ab illo inventore veritatis et quasi architecto beatae vitae dicta sunt explicabo. Nemo enim ipsam voluptatem quia voluptas sit aspernatur aut odit aut fugit, sed quia consequuntur magni dolores eos qui ratione voluptatem sequi nesciunt. Neque porro quisquam est, qui dolorem ipsum quia dolor sit amet, consectetur, adipisc.</p>
  <div class="abs btn">Read More</div>
  <div class="abs rule" style="left:56px;top:678px;width:692px"></div>
</section>

<section>
  <h2 class="abs section-title" style="top:709px;font-weight:400">Featured <span>Video’s</span></h2>
  <div class="abs video-main" role="img" aria-label="Sunset over a farm field">
    <svg class="play" style="top:45%" width="46" height="46" viewBox="0 0 46 46"><circle cx="23" cy="23" r="23" fill="#222" opacity=".8"/><path d="M17 12l16 11-16 11z" fill="#eee"/></svg>
  </div>
  <svg class="abs video-bar" viewBox="0 0 344 20">
    <path d="M8 5l9 5-9 5z" fill="#333"/>
    <rect x="30" y="7" width="176" height="6" rx="3" fill="#333"/>
    <rect x="30" y="7" width="18" height="6" rx="3" fill="#4aa3df"/>
    <circle cx="48" cy="10" r="4.5" fill="#eee" stroke="#555"/>
    <text x="209" y="13" font-size="6.5" font-family="Arimo,Arial,sans-serif" fill="#222">0.00 / 9.29</text>
    <path d="M256 8h3l4-3v10l-4-3h-3z" fill="#333"/>
    <rect x="271" y="7" width="44" height="6" rx="3" fill="#333"/>
    <circle cx="312" cy="10" r="3.5" fill="#eee" stroke="#555"/>
    <rect x="330" y="6" width="8" height="8" fill="none" stroke="#333"/>
  </svg>
  <div class="abs thumb" style="left:448px;top:744px;background:linear-gradient(135deg,#d8c9a5,#c9a24c 50%,#6f8a3a)" role="img" aria-label="Corn kernels spilling from a sack">
    <svg class="play" width="30" height="30" viewBox="0 0 30 30"><circle cx="15" cy="15" r="15" fill="#222" opacity=".85"/><path d="M11 8l11 7-11 7z" fill="#eee"/></svg></div>
  <div class="abs thumb" style="left:591px;top:744px;background:radial-gradient(circle,#d9a865 0%,#c69a62 35%,#c5b8a8 60%,#bfb3a6 100%)" role="img" aria-label="Bowl of soybeans">
    <svg class="play" width="30" height="30" viewBox="0 0 30 30"><circle cx="15" cy="15" r="15" fill="#222" opacity=".85"/><path d="M11 8l11 7-11 7z" fill="#eee"/></svg></div>
  <div class="abs thumb" style="left:448px;top:848px;background:linear-gradient(180deg,#3a69c2 0%,#9ab7e0 35%,#c7b23a 55%,#3f7a1a 100%)" role="img" aria-label="Crop rows under a bright sky">
    <svg class="play" width="30" height="30" viewBox="0 0 30 30"><circle cx="15" cy="15" r="15" fill="#222" opacity=".85"/><path d="M11 8l11 7-11 7z" fill="#eee"/></svg></div>
  <div class="abs thumb" style="left:591px;top:848px;background:linear-gradient(180deg,#6d7f96 0%,#a9b0b5 30%,#b58d25 55%,#d2a21e 100%)" role="img" aria-label="Golden soybean field">
    <svg class="play" width="30" height="30" viewBox="0 0 30 30"><circle cx="15" cy="15" r="15" fill="#222" opacity=".85"/><path d="M11 8l11 7-11 7z" fill="#eee"/></svg></div>
  <div class="abs rule" style="left:58px;top:978px;width:694px"></div>
</section>

<section>
  <h3 class="abs partners-title" style="font-weight:400">Neque porro <span>quisquam</span></h3>
  <p class="abs partners-text">Sed ut perspiciatis unde omnis iste natus error sit voluptatem accusantium doloremque laudantium, totam rem aperiam, eaque ipsa.</p>
  <div class="abs partner" style="left:356px;font-size:11px"><span class="dot" style="background:#d52b1e"></span>Northfield Agri</div>
  <div class="abs partner" style="left:494px"><span class="dot" style="background:var(--green)"></span>Vantage</div>
  <div class="abs partner" style="left:630px"><span class="dot" style="background:var(--orange)"></span>Marlow</div>
</section>

<footer class="abs site-footer"></footer>
<div class="abs social" style="left:51px;background:#3b5998" role="img" aria-label="Social profile"></div>
<div class="abs social" style="left:80px;background:#2fa3d6" role="img" aria-label="Social profile"></div>
<div class="abs social" style="left:108px;background:#8b6f55" role="img" aria-label="Social profile"></div>
<div class="abs social" style="left:136px;background:#c4302b" role="img" aria-label="Social profile"></div>
<p class="abs copyright">Copyrights 2012-2014 Yoursite All Right Reserved.</p>
<p class="abs newsletter-title">Newsletter sign up..</p>
<div class="abs newsletter-input">Enter your Email..</div>
<svg class="abs newsletter-btn" viewBox="0 0 22 21"><path d="M9 6l5 4.5-5 4.5" fill="none" stroke="#fff" stroke-width="1.2"/></svg>

</body>
</html>
```